Business Coach needs an elegant business card design

I need a business card design based around my logo for color and to look like a millionaire dollar coach. Incorporate the color of my logo with something creative and attractive that stands out. I am focused on high end companies and the card must look and feel that way.

Target Market(s)

High End Companies and Business Owners - Training People to become millionaires

Industry/Entity Type

Business

Requirements
Must have
• Front -
Logo (attached file) - Website (marlowkeeve.com) - Name (Marlow Keeve) Phone (555.201.7746) - Email (marlow@marlowkeeve.com) (My Title - Success Coach)
Back -
Slogan - Vision (see it) . Action (do it) . Transformation (be it)
Website - Learn More @ marlowkeeve.com

Creative High End Look!
Nice to have
Should not have
• Cheap standard look
nothing traditional

```html
<!DOCTYPE html>
<html lang="en">
<head>
<meta charset="utf-8">
<title>Marlow Keeve Coaching – Business Card</title>
<link rel="stylesheet" href="https://fonts.googleapis.com/css2?family=Cinzel:wght@400;600;700&display=swap">
<style>
  :root {
    --backdrop: #e6e6e8;
    --paper: #f4f4f3;
    --navy: #1c2857;
    --navy-deep: #0e1736;
    --navy-light: #25346a;
    --band-text: #8c919c;
    --ink: #1c2857;
    --ink-soft: #2a2f3d;
    --white: #ffffff;
    --muted-white: #d9dce6;
  }
  * { box-sizing: border-box; margin: 0; padding: 0; }
  html, body {
    width: 1200px; height: 720px; overflow: hidden;
    background: var(--backdrop);
    font-family: "Cinzel", serif;
  }
  .canvas { position: relative; width: 1200px; height: 720px; }

  .card {
    position: absolute; top: 242px;
    width: 420px; height: 238px; overflow: hidden;
  }

  /* Front */
  .card-front { left: 147px; background: var(--paper); }
  .front-band {
    position: absolute; left: 0; top: 49px; width: 100%; height: 65px;
    background: var(--navy);
  }
  .front-footer-band {
    position: absolute; left: 0; bottom: 0; width: 100%; height: 12px;
    background: var(--navy);
  }
  .band-word {
    position: absolute; top: 49px; height: 65px; line-height: 65px;
    font-size: 16px; font-weight: 700; color: var(--band-text);
    letter-spacing: 0.3px; white-space: nowrap; text-align: center;
  }
  .band-word-name { left: 4px; width: 152px; }
  .band-word-coaching { left: 264px; width: 152px; }
  .brand-dot {
    position: absolute; left: 162px; top: 34px;
    width: 96px; height: 96px; border-radius: 50%;
    background: var(--navy); border: 4px solid var(--white);
  }
  .holder {
    position: absolute; left: 0; width: 100%; text-align: center;
  }
  .holder-name {
    top: 142px; font-size: 14px; font-weight: 700; color: var(--ink);
    letter-spacing: 0.5px;
  }
  .holder-title {
    top: 159px; font-size: 9.5px; color: var(--ink-soft);
  }
  .contact-row {
    position: absolute; top: 197px; left: 0; width: 100%;
    display: flex; justify-content: center; align-items: center;
    font-size: 9.5px; color: var(--ink-soft);
  }
  .contact-item { padding: 0 16px; white-space: nowrap; }
  .contact-divider {
    width: 1.5px; height: 18px; background: var(--navy);
  }

  /* Back */
  .card-back {
    left: 633px;
    background: linear-gradient(150deg, var(--navy-light) 0%, var(--navy) 45%, var(--navy-deep) 100%);
  }
  .back-mark {
    position: absolute; left: 20px; top: 96px;
    width: 46px; height: 46px; border-radius: 50%;
    border: 2px solid var(--white);
  }
  .back-brand {
    position: absolute; left: 73px; top: 101px;
    color: var(--white); font-weight: 400; text-align: center;
  }
  .back-brand-name { font-size: 18px; line-height: 22px; display: block; white-space: nowrap; }
  .back-brand-sub { font-size: 9px; letter-spacing: 3px; line-height: 12px; display: block; }
  .slogan {
    position: absolute; left: 270px; top: 95px;
    font-size: 12px; line-height: 16px; color: var(--muted-white);
  }
  .slogan-line { display: block; white-space: nowrap; }
  .slogan-accent { font-style: italic; }
  .back-url {
    position: absolute; left: 0; top: 216px; width: 100%; text-align: center;
    font-size: 8.5px; color: var(--muted-white); letter-spacing: 0.3px;
  }
</style>
</head>
<body>
<main class="canvas">
  <section class="card card-front" aria-label="Card front">
    <div class="front-band"></div>
    <span class="band-word band-word-name">MARLOW KEEVE</span>
    <span class="band-word band-word-coaching">COACHING</span>
    <div class="brand-dot"></div>
    <p class="holder holder-name">Marlow Keeve</p>
    <p class="holder holder-title">Success Coach</p>
    <div class="contact-row">
      <span class="contact-item">555.201.7746</span>
      <span class="contact-divider"></span>
      <span class="contact-item">marlow@marlowkeeve.com</span>
      <span class="contact-divider"></span>
      <span class="contact-item">marlowkeeve.com</span>
    </div>
    <div class="front-footer-band"></div>
  </section>

  <section class="card card-back" aria-label="Card back">
    <div class="back-mark"></div>
    <p class="back-brand">
      <span class="back-brand-name">Marlow Keeve</span>
      <span class="back-brand-sub">COACHING</span>
    </p>
    <p class="slogan">
      <span class="slogan-line">See What You Want</span>
      <span class="slogan-line">Do What It Takes</span>
      <span class="slogan-line slogan-accent">Live Your Vision!</span>
    </p>
    <p class="back-url">www.marlowkeeve.com</p>
  </section>
</main>
</body>
</html>
```